National Female Non-profit Business Card

We need a business card design as soon as possible for a non-profit organisation called Meadow to Summit. Our aim is to empower leadership potential in rural female teens.
The business card should have our logo on the one side and then information on the other side, including name, job title, email address, phone number and website (www.meadowtosummit.com.au) and our twitter handle @MeadowSummit
It should use the colours white, coral (#f04a50) and orange (#f68e4e). The font used in the logo is Raleway.
The hashtag #YoungVoicesRise could be used.
It should be bright, chic and crisp. Our logo is attached.

Target Market(s)
We will be handing the cards out to politicians and senior executives. However, as we're a non-profit for young women, they also need to reflect femininity and youth.
Industry/Entity Type
Non-Profit
Look and feel

```html
<!DOCTYPE html>
<html lang="en">
<head>
<meta charset="utf-8">
<title>Meadow to Summit – Business Card</title>
<link rel="stylesheet" href="https://fonts.googleapis.com/css2?family=Arimo:wght@400&family=Raleway:wght@400&display=swap">
<style>
  :root {
    --backdrop: #2b2b2b;
    --paper: #ffffff;
    --coral: #e8324f;
    --orange: #f18c44;
    --ink: #333333;
    --card-w: 525px;
    --card-h: 300px;
  }
  * { box-sizing: border-box; margin: 0; padding: 0; }
  html, body {
    width: 1200px;
    height: 900px;
    overflow: hidden;
    background: var(--backdrop);
  }
  .canvas {
    position: relative;
    width: 1200px;
    height: 900px;
  }
  .card {
    position: absolute;
    width: var(--card-w);
    height: var(--card-h);
    overflow: hidden;
  }
  .card--front { left: 277px; top: 123px; background: var(--paper); }
  .card--back  { left: 397px; top: 467px; background: var(--coral); }

  /* small brand line, top left of front */
  .brand {
    position: absolute;
    left: 16px;
    top: 76px;
    display: flex;
    align-items: center;
    gap: 6px;
    font-family: "Raleway", sans-serif;
    font-weight: 400;
    font-size: 12px;
    letter-spacing: 0.2px;
    color: var(--coral);
    text-transform: uppercase;
  }
  .brand__dot {
    width: 7px; height: 7px;
    border-radius: 50%;
    background: var(--orange);
  }

  /* large brand mark area, top right of front */
  .brand-feature {
    position: absolute;
    right: 18px;
    top: 40px;
    width: 190px;
    display: flex;
    flex-direction: column;
    align-items: flex-end;
    gap: 14px;
  }
  .brand-feature__dot {
    width: 34px; height: 34px;
    border-radius: 50%;
    background: var(--orange);
  }
  .brand-feature__name {
    font-family: "Raleway", sans-serif;
    font-weight: 400;
    font-size: 26px;
    line-height: 1.15;
    text-align: right;
    text-transform: uppercase;
    color: var(--coral);
  }

  .person__name {
    position: absolute;
    left: 15px;
    top: 107px;
    font-family: "Arimo", sans-serif;
    font-weight: 400;
    font-size: 23px;
    color: var(--ink);
  }
  .person__title {
    position: absolute;
    left: 91px;
    top: 135px;
    font-family: "Arimo", sans-serif;
    font-size: 8.5px;
    color: var(--ink);
    text-transform: uppercase;
  }
  .contacts {
    position: absolute;
    left: 17px;
    top: 174px;
    list-style: none;
    font-family: "Arimo", sans-serif;
    font-size: 15px;
    color: var(--ink);
  }
  .contacts__item {
    display: flex;
    align-items: center;
    height: 29px;
  }
  .contacts__icon {
    width: 20px; height: 20px;
    margin-right: 10px;
    flex: none;
  }
  .front-swoosh, .back-arc {
    position: absolute;
    left: 0; top: 0;
    width: var(--card-w);
    height: var(--card-h);
  }

  /* back */
  .back-brand {
    position: absolute;
    left: 0; right: 0;
    top: 62px;
    display: flex;
    flex-direction: column;
    align-items: center;
    gap: 16px;
  }
  .back-brand__dot {
    width: 36px; height: 36px;
    border-radius: 50%;
    background: var(--paper);
  }
  .back-brand__name {
    font-family: "Raleway", sans-serif;
    font-weight: 400;
    font-size: 30px;
    text-transform: uppercase;
    color: var(--paper);
  }
  .back-url {
    position: absolute;
    left: 0; right: 0;
    top: 244px;
    text-align: center;
    font-family: "Arimo", sans-serif;
    font-size: 19px;
    color: var(--paper);
  }
  .back-handle {
    position: absolute;
    left: 0; right: 0;
    top: 272px;
    text-align: center;
    font-family: "Arimo", sans-serif;
    font-size: 13px;
    color: var(--paper);
  }
</style>
</head>
<body>
<main class="canvas">

  <section class="card card--front" aria-label="Business card front">
    <div class="brand"><span class="brand__dot"></span>Meadow to Summit</div>

    <div class="brand-feature">
      <span class="brand-feature__dot"></span>
      <p class="brand-feature__name">Meadow<br>to Summit</p>
    </div>

    <h1 class="person__name">Your Name</h1>
    <p class="person__title">Job Title</p>

    <ul class="contacts">
      <li class="contacts__item">
        <svg class="contacts__icon" viewBox="0 0 20 20" fill="none" stroke="var(--ink)" stroke-width="1.3">
          <rect x="1.5" y="4.5" width="17" height="11"/>
          <path d="M1.5 4.5 L10 11 L18.5 4.5"/>
        </svg>
        name@meadowtosummit.com.au
      </li>
      <li class="contacts__item">
        <svg class="contacts__icon" viewBox="0 0 20 20">
          <path fill="var(--ink)" d="M6 2 L8.5 6.2 L7 7.8 C7.6 10 9 12.3 10.9 13.9 L12.5 12.6 L15.6 16 L13.6 18 C8.5 17 4.5 10.5 4.3 4 Z"/>
        </svg>
        0000 000 000
      </li>
      <li class="contacts__item">
        <svg class="contacts__icon" viewBox="0 0 20 20" fill="none" stroke="var(--ink)" stroke-width="1.2">
          <circle cx="10" cy="10" r="8"/>
          <ellipse cx="10" cy="10" rx="3.6" ry="8"/>
          <path d="M2 10 H18 M3.2 6 H16.8 M3.2 14 H16.8"/>
        </svg>
        www.meadowtosummit.com.au
      </li>
    </ul>

    <svg class="front-swoosh" viewBox="0 0 525 300" aria-hidden="true">
      <path fill="var(--coral)" d="M166 300 Q320 244 525 248 L525 267 Q330 260 166 300 Z"/>
    </svg>
  </section>

  <section class="card card--back" aria-label="Business card back">
    <div class="back-brand">
      <span class="back-brand__dot"></span>
      <p class="back-brand__name">Meadow to Summit</p>
    </div>
    <svg class="back-arc" viewBox="0 0 525 300" aria-hidden="true">
      <path fill="var(--orange)" d="M0 262 Q262 174 525 262 L525 300 L0 300 Z"/>
      <path fill="var(--paper)" d="M0 255 Q262 140 525 255 L525 262 Q262 174 0 262 Z"/>
    </svg>
    <p class="back-url">www.meadowtosummit.com.au</p>
    <p class="back-handle">@MeadowSummit</p>
  </section>

</main>
</body>
</html>
```